Flyer für Hersteller von Designertischen
Zielgruppe
Wir bauen Designer Tische, unser Zielgruppe liegt zwischen 35 und 50 Jahren
Aufgabenstellung
Wir legen Wert auf ein minimales Design, gerne in dem Stil unserer Website

```html
<!DOCTYPE html>
<html lang="de">
<head>
<meta charset="utf-8">
<title>Lindqvist Manufaktur – Flyer</title>
<link href="https://fonts.googleapis.com/css2?family=Poppins:ital,wght@0,300;0,400;0,600;0,700;1,400&family=Raleway:wght@400;500&display=swap" rel="stylesheet">
<style>
  :root {
    --backdrop: #c8c8c8;
    --bronze: #935d00;
    --ink: #000000;
    --paper: #f4f5f7;
    --white: #ffffff;
    --wood-light: #c9a47a;
    --wood-mid: #9c7449;
    --wood-dark: #5b4530;
  }
  * { margin: 0; padding: 0; box-sizing: border-box; }
  html, body { width: 1200px; height: 1200px; overflow: hidden; }
  body {
    background: var(--backdrop);
    font-family: 'Poppins', sans-serif;
    position: relative;
  }
  .flyer {
    position: absolute;
    left: 254px; top: 115px;
    width: 693px; height: 970px;
    background: var(--paper);
    overflow: hidden;
  }
  .hero {
    position: absolute; left: 0; top: 0; width: 693px; height: 388px;
  }
  .hero-photo {
    position: absolute; inset: 0;
    background:
      linear-gradient(90deg, rgba(255,255,255,0.95) 0%, rgba(255,255,255,0.75) 25%, rgba(255,255,255,0.15) 55%, rgba(255,255,255,0) 70%),
      linear-gradient(160deg, #e8e4dc 0%, var(--wood-light) 35%, var(--wood-mid) 60%, var(--wood-dark) 85%, #2b3a6b 100%);
  }
  .brand {
    position: absolute; left: 57px; top: 66px;
    display: flex; align-items: center; gap: 8px;
    font-weight: 600; font-size: 13px; letter-spacing: 1px; color: var(--ink);
  }
  .brand-dot {
    width: 22px; height: 22px; border: 2px solid var(--ink); border-radius: 50%;
  }
  .headline {
    position: absolute; left: 55px; top: 160px;
    font-size: 53px; line-height: 65px; color: var(--ink);
    text-transform: uppercase;
  }
  .headline .accent { display: block; font-weight: 700; color: var(--bronze); }
  .headline .light { display: block; font-weight: 300; }
  .about {
    position: absolute; left: 0; top: 388px; width: 415px; height: 190px;
    background: var(--bronze); color: var(--white);
    padding: 32px 15px 0 55px;
  }
  .section-title { font-weight: 700; font-size: 19px; line-height: 24px; }
  .about p, .why p {
    font-size: 9.6px; line-height: 12.3px; text-align: justify; margin-top: 12px;
  }
  .why {
    position: absolute; left: 415px; top: 388px; width: 278px; height: 190px;
    background: var(--ink); color: var(--white);
    padding: 30px 47px 0 24px;
  }
  .why p { margin-top: 14px; }
  .gallery-bar {
    position: absolute; left: 0; top: 578px; width: 265px; height: 38px;
    background: var(--ink); color: var(--white);
    padding-left: 55px;
    font-weight: 700; font-size: 17px; letter-spacing: 3.5px; line-height: 38px;
  }
  .gallery-note {
    position: absolute; left: 278px; top: 592px;
    font-style: italic; font-size: 10.5px; letter-spacing: 0.3px; color: var(--ink);
  }
  .gallery-item {
    position: absolute; top: 654px; width: 161px; height: 185px;
  }
  .g1 { left: 61px; background: linear-gradient(150deg, #b99b78, #8a6a48 60%, #6c5a48); }
  .g2 { left: 265px; background: linear-gradient(180deg, #d6d8db 0%, #cfc7b9 55%, #ddd2c0 100%); }
  .g3 { left: 469px; background: linear-gradient(180deg, #eceef0 0%, #c9a57a 45%, #7b3e1e 100%); }
  .address {
    position: absolute; left: 0; top: 870px; width: 693px; text-align: center;
    font-family: 'Raleway', sans-serif; font-size: 11px; line-height: 14px;
    letter-spacing: 2.2px; color: var(--bronze);
  }
  .footer {
    position: absolute; left: 0; top: 922px; width: 693px; height: 48px;
    background: var(--bronze); color: var(--white);
    text-align: center; line-height: 48px;
    font-family: 'Raleway', sans-serif; font-size: 10.5px; letter-spacing: 3px;
  }
</style>
</head>
<body>
  <main class="flyer">
    <section class="hero">
      <div class="hero-photo" role="img" aria-label="Esstisch aus rustikalem Altholz in einem hellen Wohnraum mit Pflanzen"></div>
      <div class="brand"><span class="brand-dot"></span>Lindqvist Manufaktur</div>
      <h1 class="headline">
        <span class="accent">Möbel die</span>
        <span class="light">Geschichten</span>
        <span class="light">erzählen</span>
      </h1>
    </section>

    <section class="about">
      <h2 class="section-title">Über mich</h2>
      <p>Ich bin Jonas Lindqvist und Gründer der Lindqvist Manufaktur. Mein Vater war Holzbildhauer, wodurch ich bereits in früher Kindheit mit dem Material Holz in Kontakt kam und seither Techniken der Holzbearbeitung erlernte. Inzwischen habe ich mich auf die Arbeit mit Holzmonolithen spezialisiert, also die Herstellung von Esstischen die aus einer einzigen großen Bohle geschaffen werden. Darüber hinaus stellen wir leidenschaftlich gerne Couchtische, Waschtischplatten und Konferenztische her.</p>
    </section>

    <section class="why">
      <h2 class="section-title">Warum uns wählen?</h2>
      <p>Unsere Leidenschaft ist es, zeitlose und langlebige Möbel zu schaffen. Jeder unserer Tische wird mit Sorgfalt und Liebe zum Detail gefertigt, um ein Leben lang zu bestehen. Qualität und Beständigkeit sind dabei unser oberstes Ziel.</p>
    </section>

    <div class="gallery-bar">GALERIE</div>
    <p class="gallery-note">Finden Sie alle Optionen, die im Bereich des Schlüssels liegen.</p>

    <div class="gallery-item g1" role="img" aria-label="Nahaufnahme einer Eichen-Tischplatte mit Baumkante"></div>
    <div class="gallery-item g2" role="img" aria-label="Couchtisch aus Massivholz auf schwarzem Stahlgestell"></div>
    <div class="gallery-item g3" role="img" aria-label="Massivholz-Tisch auf keilförmigen Rostbeinen"></div>

    <p class="address">Lindqvist Manufaktur<br>Ahornweg 14, 70180 Stuttgart</p>

    <footer class="footer">www.lindqvist-manufaktur.de</footer>
  </main>
</body>
</html>
```